Brevin Electric Ltd

Looking for a single page website and Facebook page design. I am an electrical contractor based on Vancouver Island. I do service, custom homes, residential and commercial installations. My company just started out, so I don't have any pictures of installs yet. I have 25 years experience. I would like the colors to be my logo colors black and I have a black Torvik Ridgeman that will be my vehicle which I will have a wrap for.
Updates

I just posted the contest today, not sure why the deadline is the same day.

Went on vacation/holiday

Industry/Entity Type

Electrician

Requirements
Must have
• Services provided, About me section, quote section,
Nice to have
• I am not quite sure yet, I need to see some designs first .

```html
<!DOCTYPE html>
<html lang="en">
<head>
<meta charset="utf-8">
<title>Brevin Electric Ltd – Cover Banner</title>
<link href="https://fonts.googleapis.com/css2?family=Montserrat:wght@600;700&family=Open+Sans:wght@400;600&display=swap" rel="stylesheet">
<style>
  :root {
    --ink: #050505;
    --white: #ffffff;
    --amber: #f6be15;
    --soft-white: #e9e9e9;
    --photo-dark: #4a5258;
    --photo-mid: #9aa3a8;
    --photo-light: #d7dcdf;
    --shirt: #f08a2a;
  }
  * { margin: 0; padding: 0; box-sizing: border-box; }
  html, body { width: 1200px; height: 444px; overflow: hidden; background: var(--white); }
  .banner {
    position: relative;
    width: 1200px;
    height: 444px;
    background: var(--ink);
    overflow: hidden;
    font-family: "Open Sans", Arial, sans-serif;
    color: var(--white);
  }
  .banner__art { position: absolute; inset: 0; }
  .brand-mark {
    position: absolute;
    left: 166px;
    top: 92px;
    display: flex;
    align-items: center;
    gap: 18px;
  }
  .brand-mark__dot {
    width: 60px;
    height: 60px;
    border-radius: 50%;
    background: var(--amber);
  }
  .brand-mark__name {
    font-family: "Montserrat", Arial, sans-serif;
    font-weight: 700;
    font-size: 40px;
    letter-spacing: 2px;
    color: var(--white);
  }
  .headline {
    position: absolute;
    left: 74px;
    top: 226px;
    font-family: "Montserrat", Arial, sans-serif;
    font-weight: 600;
    font-size: 31px;
    letter-spacing: 0.5px;
    color: var(--white);
    white-space: nowrap;
  }
  .headline__accent { color: var(--amber); }
  .tagline {
    position: absolute;
    left: 74px;
    top: 281px;
    width: 470px;
    font-size: 16.5px;
    line-height: 26px;
    color: var(--white);
  }
  .cta {
    position: absolute;
    left: 74px;
    top: 362px;
    width: 79px;
    height: 21px;
    border-radius: 3px;
    background: var(--amber);
    color: var(--white);
    font-family: "Montserrat", Arial, sans-serif;
    font-weight: 700;
    font-size: 11.5px;
    letter-spacing: 0.8px;
    display: flex;
    align-items: center;
    justify-content: center;
  }
  .contact-row {
    position: absolute;
    left: 74px;
    top: 389px;
    width: 470px;
    height: 20px;
    display: flex;
    align-items: center;
    font-size: 13px;
    letter-spacing: 1.3px;
  }
  .contact-row__site { width: 262px; }
  .social { display: flex; gap: 5px; margin-right: 10px; }
  .social__dot {
    width: 18px;
    height: 18px;
    border-radius: 50%;
    background: var(--amber);
  }
  .contact-row__handle { letter-spacing: 1.3px; }
</style>
</head>
<body>
  <main class="banner">
    <svg class="banner__art" width="1200" height="444" viewBox="0 0 1200 444">
      <defs>
        <linearGradient id="photo-tone" x1="0" y1="0" x2="1" y2="1">
          <stop offset="0" stop-color="var(--photo-mid)"/>
          <stop offset="0.45" stop-color="var(--photo-light)"/>
          <stop offset="1" stop-color="var(--photo-dark)"/>
        </linearGradient>
        <radialGradient id="shirt-glow" cx="0.2" cy="0.75" r="0.45">
          <stop offset="0" stop-color="var(--shirt)" stop-opacity="0.9"/>
          <stop offset="1" stop-color="var(--shirt)" stop-opacity="0"/>
        </radialGradient>
      </defs>
      <polygon class="accent-white" points="588,0 850,0 770,120" fill="var(--soft-white)"/>
      <polygon class="accent-amber" points="744,0 846,0 718,210" fill="var(--amber)"/>
      <polygon class="accent-amber-low" points="760,444 800,380 830,444" fill="var(--amber)"/>
      <g role="img" aria-label="Photo of an electrician in an orange shirt and white gloves wiring a distribution panel">
        <polygon points="846,0 1200,0 1200,444 790,444 708,228" fill="url(#photo-tone)"/>
        <polygon points="846,0 1200,0 1200,444 790,444 708,228" fill="url(#shirt-glow)"/>
      </g>
      <polygon class="accent-white-corner" points="1120,0 1200,0 1200,40" fill="var(--soft-white)"/>
      <polygon class="accent-amber-edge" points="1200,150 1128,250 1160,444 1200,444" fill="var(--amber)"/>
    </svg>

    <div class="brand-mark">
      <span class="brand-mark__dot"></span>
      <span class="brand-mark__name">BREVIN</span>
    </div>

    <h1 class="headline">BREVIN <span class="headline__accent">ELECTRIC</span> Ltd</h1>
    <p class="tagline">We do service, custom homes, residential and commercial installations</p>

    <div class="cta">JOIN US</div>

    <div class="contact-row">
      <span class="contact-row__site">www.websitename.com</span>
      <span class="social" aria-label="Social links">
        <span class="social__dot"></span>
        <span class="social__dot"></span>
        <span class="social__dot"></span>
        <span class="social__dot"></span>
      </span>
      <span class="contact-row__handle">/ brandname</span>
    </div>
  </main>
</body>
</html>
```